依頼概要
■依頼目的/概要
Tolino(ブログ)内で「診断レポート」を提供しますので、
表紙デザイン作成をお願いいたします。

■納品物
下記での納品をお願いいたします。
JPEG形式
横1600ピクセル×縦2560ピクセル

■診断レポートの内容
<レポートのタイトル>
40代からのあなたの経験を徹底的に活かすための5つの習慣 ビジネスもプライベートも充実した毎日を手に入れる

<キャッチコピー>
以下の文言の中から組み合わせるか、選んで載せてください。

・他人軸で生きる辛さから脱却しないと人生に悔いが残る!

・人生の転機のヒントが得られる!

・自分らしく生きるヒントが分かる!

・ハンディや持病を抱えながらも一部上場企業に貢献し、独立・起業したコーチが伝える

<著者名>
・著者名 前田芳典(ライフコーチ) M&R 合同会社 代表

■デザイン要望
・本のタイトル/キャッチコピー/著者名の反映をお願い致します。

・読者は40代50代60代の自分らしく生きようとしている人です。

・これからの人生設計を踏まえた考え方や捉え方を書いたレポートですので、
「ビジネス書の表紙」というイメージでお願いします。

・タイトル文字数が、ちょっと多いのですが、
できるだけ文字を認識しやすいようにしたいです。

・未来の人生に新たな可能性が見えるイメージです。

・タイトルの中では、「強み」「充実した人生」「生かす」
あたりが、目立つようにしたいです。

<表現したいイメージなど>
・信頼感
・ビジネス書っぽい感じ
・ベストセラーのマーケティング関連ビジネス書など、
どこかで見たことがあるような感じの安心感
・カラーの希望などはありません。お任せで。

<利用画像について>
イラスト等素材を使用される場合には、
商用利用可の素材をお願いします。

■その他、デザインを考えるのに必要な情報などありましたら、
お答えしますので、遠慮なく聞いて下さい。
■ 選んだ理由

皆様のレベルが高くて本当に嬉しい限りです。選定したポイントは、2案を出してもらいながら、シンプルで分かりやすく、タイトル周りの文字もメリハリがあり、「強み」「生かす」が強調されており、「人生の転機」も目を引き付けました。「充実した人生」も金色で表現しているところにデザインの秀逸さを感じました。また、ビジネス本という視点からも、青白でシンプルに構成され伝わりやすい表現がベストセラーにも多いので、そこにも共感をしました。一部修正依頼をさせていただいた対応も迅速丁寧で感謝しております。

■ 提案者全員のお礼・コメント

皆様、多くの素晴らしいご提案をいただき感謝しております。本当にありがとうございました。次回の依頼する際におきましてもご協力いただきますようお願いいたします。今後ともどうぞよろしくお願いいたします。

```html
<!DOCTYPE html>
<html lang="ja">
<head>
<meta charset="utf-8">
<title>40代からのあなたの経験を徹底的に活かすための5つの習慣</title>
<link href="https://fonts.googleapis.com/css2?family=Noto+Sans+JP:wght@500;700;900&display=swap" rel="stylesheet">
<style>
  :root {
    --ink: #111111;
    --paper: #ffffff;
    --accent-red: #e3141c;
    --photo-dark: #14171d;
    --photo-mid: #2a2f38;
    --badge-pink: #f7d6ea;
    --badge-blue: #d4e6f8;
  }
  * { margin: 0; padding: 0; box-sizing: border-box; }
  html, body { width: 749px; height: 1200px; overflow: hidden; background: var(--paper); }
  .cover {
    position: relative;
    width: 749px;
    height: 1200px;
    font-family: "Noto Sans JP", sans-serif;
    color: var(--ink);
    overflow: hidden;
    background: var(--paper);
  }
  .hero-photo {
    position: absolute;
    left: 0; top: 0;
    width: 749px; height: 562px;
    background:
      radial-gradient(ellipse at 72% 30%, #4a505b 0%, var(--photo-mid) 30%, var(--photo-dark) 70%),
      var(--photo-dark);
  }
  .title { color: var(--paper); font-weight: 900; }
  .title-line {
    position: absolute;
    left: 26px;
    white-space: nowrap;
    line-height: 1;
  }
  .line-age { top: 30px; font-size: 50px; font-weight: 700; }
  .line-asset { top: 90px; font-size: 52px; font-weight: 700; }
  .line-extent { top: 158px; font-size: 72px; }
  .line-apply { top: 248px; font-size: 64px; }
  .line-apply .key { font-size: 94px; }
  .line-habits { top: 386px; font-size: 98px; }
  .line-habits .num { font-size: 132px; }
  .line-habits .key { font-size: 138px; }
  .title-red { color: var(--accent-red); }
  .subtitle { font-weight: 900; }
  .subtitle-line {
    position: absolute;
    left: 28px;
    white-space: nowrap;
    line-height: 1;
  }
  .subtitle-lead { top: 578px; font-size: 42px; }
  .subtitle-main-1 { top: 640px; font-size: 94px; }
  .subtitle-main-2 { top: 748px; font-size: 94px; }
  .badge {
    position: absolute;
    left: 494px; top: 862px;
    width: 240px; height: 240px;
    border-radius: 50%;
    background: linear-gradient(135deg, var(--badge-pink), var(--badge-blue));
    display: flex; align-items: center; justify-content: center;
    text-align: center;
    font-weight: 700;
    font-size: 29px;
    line-height: 1.5;
  }
  .author-role {
    position: absolute;
    left: 28px; top: 1018px;
    font-size: 21px; font-weight: 700;
    white-space: nowrap;
  }
  .author-name {
    position: absolute;
    left: 24px; top: 1062px;
    font-size: 84px; font-weight: 900;
    letter-spacing: 4px; line-height: 1;
    white-space: nowrap;
  }
</style>
</head>
<body>
<main class="cover">
  <div class="hero-photo" role="img" aria-label="暗い背景に立つスーツ姿のビジネスマンの写真"></div>

  <h1 class="title">
    <span class="title-line line-age">40代からの</span>
    <span class="title-line line-asset">あなたの経験を</span>
    <span class="title-line line-extent">徹底的に</span>
    <span class="title-line line-apply"><span class="key title-red">活かす</span>ための</span>
    <span class="title-line line-habits"><span class="num">5</span>つの<span class="key title-red">習慣</span></span>
  </h1>

  <p class="subtitle">
    <span class="subtitle-line subtitle-lead">ビジネスもプライベートも</span>
    <span class="subtitle-line subtitle-main-1">充実した毎日を</span>
    <span class="subtitle-line subtitle-main-2">手に入れる</span>
  </p>

  <div class="badge"><p>人生の<br>転機のヒントが<br>得られる!</p></div>

  <p class="author-role">M&amp;R 合同会社代表 ライフコーチ</p>
  <p class="author-name">前田 芳典</p>
</main>
</body>
</html>
```